Mobile Marketing Business needs a UNIQUE web design that makes users stop, adore and engage!

Unique web design for a new division of our company. Based in Los Angeles, TornaCell is a mobile marketing company offering mobile optimized websites, sms marketing, strategic and analytic consultation services. We are a b2b model targeting a wide range of industries and business sizes. Our parent company is Harbrook Digital. Tornacell needs to reflect a progressive nature, confidence, and experience - yet affordable to any business that wants to reach the mobile consumer. We want to avoid a dark website or one that is too bland. The colors should be strong, yet not overly so.

Layout should be clean, focused, - avoiding a cluttered home page. Visitors should recognize WE ARE mobile marketing - it should resonate that WE differ from competitors - Site design should resonate our brand! We've noticed competitors sites start to look and feel like the same - where the visitor may quickly exit from the home page or first inner page. There are some sites that differ which we've listed below.

The audience will range from sophisticated marketers to a local business operator who is not web savvy. The site should welcome all - not intimidate some while wowing others. We understand it's difficult for websites to be a "one size fits all" - but in reviewing competitive sites, it's apparent no one site really leaves any key impression. We'd like Tornacell to be the one.

The site should invite user to engage with the site and compel them to contact us for a demo for a better understanding of how mobiele marketing is the ultimate one 2 one sales channel that can help them improve gross sales.

Site should not be "dark" which requires using white font - we do not want "wild" or "fluorescent" colors. A tasteful, classic balance of colors that provides a comfortable experience to engage.

We realize this challenge seems .. well extremely challenging but we're quite confident there is a "design ninja" lurking out there. Are YOU the one?

Happy to provide more details and info as needed.

Sample sites that we like and feel are unique to the industry and also a site that we feel is quite basic:

www.pelvarstudio.com - clever use of banner area and using a slider to present services. However, labeling the sliders as such is a little difficult to read.

www.brantiqo.ca - clean, classic, minimalistic. Perhaps too minimal for our need but we like it. Nice use of the varying sizes and treatment of 3 promo boxes under main banner. Inner page layout is nice.

www.quarvelo.com - clever, unique. Love the call to action box (adjacent to phone) offering 3 options for next steps. Inner pages are well designed - overall site is clean, easy to read and merchandises offerings effectively.

www.brightmarshgroup.com - clean, well merchandised but home page is a bit too cluttered. good use of colors, inner page layout is simple but effective.

www.delvapost.com - clean, simple easy to follow.

www.trimesk.com - pretty basic site - in fact, you could probably replace the logo with another marketing company, etc. and the site would most likely work. We would prefer to avoid this stigma for TornaCell!!

NOTE: our logo uses a bright green that may limit it's use for mostly accents, etc. We like the contrast of colors used on www.zelnavor.com and www.paddockreel.com.au/ using the dark gray background and other colors to bring some life.

If you google "mobile marketing company", "mobile marketing services", "text messaging services", etc.. you'll notice 2 distinctive categories: amazing - like what the heck were they thinking.. and yawn - like here's another one that looks like the other..
Updates

Thank you everyone for the submissions - while they are nice, I have to say they fall into the category we were hoping to avoid (yawn, this one looks like all the other company sites)..  

Please do review the brief thoroughly - we're available if you need a specific issue addressed.  

We're still hoping a design ninja surfaces and provides a comp that makes us go "WOW'..  

cheers and good luck!

Thanks for your participation -  please stay tuned for an update to the brief along with some copy to populate the home page.  

Also... keep an eye on the project award..  we'll be increasing it after posting updates!

cheers.

UPDATE!  We have INCREASED the award in hopes of inspiring you great designers to entice your imagination and creative genetics!

PLEASE feel free to ask for further clarification or even if you want to run something by before submitting a design.  

We also have several other projects and would certainly consider those designers that truly impressed us.

As promised we're adding a bit more detail to this project.  The project requires a home and inner page layout but would like to start with the home page first.   We would also like to have a blog that differs a bit but retain some core elements of the site design.

This is a new design - our desire is to launch a website bearing an effective yet distinctive look.  Again, if you google "mobile marketing services", "mobile marketing company/companies", "mobile ..." aside from the logo varying most of the sites look the same.    We want something different..

The following may be repetitive from our brief but here goes:

Banner will focus on 3 categories - SMS/Text Marketing, Mobile Websites and Mobile Marketing:  
#1)  Headline - Did you notice how many consumers are on smartphones today?  Reach them now. 
Sub text - Mobile coupons get 10 times the redemption rate of traditional coupons
Text messages are read by 94% of recipients within 4 minutes
50% of SMS users are aged 35+ 

#2) Headline - Every day 53% of Americans use their smartphone to search the web.  Do you have a mobile optimized website?   You could be missing all these consumers each day. 
Sub text - 95% of smarthphone users search for local information 
                         70% of all mobile searches result in action within 1 hour
#3) Headline - Break through the clutter - innovative marketing campaigns distinguish your brand
Sub text - Integrate social and mobile campaigns whenever and wherever
 91% of U.S. population have a mobile device within reach 24/7

** We are open to suggestions for images or style of banner - 

Below the banner would like to have a content section featuring rotating messages titled as:
  
DID YOU KNOW? }   There are 5 times as many texters as there are Chatterly users?   < note 3-4 messages will scroll - a read more text link to an inner page for more of these facts.. 

Need 3 content sections - would prefer atypical format - not boxes, or framed areas but something different - titled:
What is a mobile website?  
Connect with mobile consumers
Mobile marketing revolution

Need:  
** a login icon for clients to access; contact us, email and text message optin - (see reference to Wendrop and Quarvelo sites from prior brief - wendrop uses creative fonts for the contact us box and email /sms optin,  quarvelo uses a creative call to action adjacent to the mobile phone with 3 options)

** to see active/ mouse over effect for navigation
** avoid a really long page - perhaps using scripts to reveal drop down boxes in content sections if necessary. 
** use of complimentary colors - keeping to white with elements of just black and green from logo gets boring
**  interesting yet not distracting shapes
** need to avoid bubble gum or flouorescent colors - note wendrop mixes colors in the main banner area in an interesting fashion. 

** need frameless design  

Again, reference the sites we liked .. and didn't like on the original brief.  Additionally we also like these sites:

1) kelbrix.com - open, expansive area - uncluttered,

2) http://presskit.daltonherald.com - love the layout and use of the black to emulate ink against white paper tying into the newspaper / brand.  We LOVE LOVE LOVE.. that sort of creativity.. in fact this is perhaps one of our favorite sites and how efficient and unique content sections, buttons, navigation, etc. is 

Looking forward to your submissions - cheers!!   

Reason: Attention all designers - this is the final extension! There are some great comps rolling in so PLEASE get your designs in soon !!!

Target Market(s)

Quite diverse actually - from local businesses (e.g., trades, professional services, retail, restaurant, hospitality, etc.) to agencies.

Industry/Entity Type

Progressive

Requirements
Must have
• Main banner of sort for messaging - would like to present 4-5 key messages that rotate/ fade on topics of SMS, mobile users, etc.
We were wondering if using mobile devices as pelvarstudio.com did to feature messages - but perhaps this limits amount of text. Also like the www.wendrop.com site with the banner rotating but also revealing portions of the slide before and after.

3-4 sections to promote key content that link to inner pages. These will feature some text - e.g., see www.brantiqo.ca - creative use of staggering box height and using script to reveal.

Main navigation = Home, Why Mobile, What We Do, Services, News (a blog), Contact. There will be 3-8 subpages for Why mobile, what we do, and services.

Footer - should contain email / text messaging sign up - see www.wendrop.com for their optin in design.

Get in Touch- again, love how www.wendrop.com has designed the "Get in Touch" call to action - not the typical button shape.

Blog - absolutely

Social icons - chatterly , workvine, and..?
Nice to have
• Not sure what we'd need here - unless you have an idea. We're open to suggestions despite our strong opinions stated so far..
Should not have
• Avoid:
anything too extreme -
avoid cartoon type illustrations
heavy use of icons
extreme colors
font that is hard to read..

```html
<!DOCTYPE html>
<html lang="en">
<head>
<meta charset="utf-8">
<title>TornaCell – Mobile Marketing</title>
<link rel="stylesheet" href="https://fonts.googleapis.com/css2?family=Arimo:wght@400;700&display=swap">
<style>
:root{
  --green:#62b244;
  --ink:#3a3a3a;
  --ink-soft:#4a4a4a;
  --nav-bg:#dcdcdc;
  --header-top:#ffffff;
  --header-bottom:#d6d6d6;
  --stage-top:#8e9aa3;
  --stage-mid:#c9d2d7;
  --stage-bottom:#b5c1c8;
  --white:#ffffff;
  --dot:#d0d0d0;
  --dot-active:#7d858b;
  --tan:#b8a47a;
}
*{box-sizing:border-box;margin:0;padding:0}
html,body{width:1200px;height:920px;overflow:hidden}
body{
  position:relative;
  font-family:"Arimo",Arial,sans-serif;
  color:var(--ink);
  background:var(--stage-mid);
}
/* Header */
.site-header{
  position:absolute;left:0;top:0;width:1200px;height:160px;
  background:linear-gradient(to bottom,var(--header-top) 0%,#f2f2f2 45%,var(--header-bottom) 100%);
}
.brand{
  position:absolute;left:107px;top:48px;
  display:flex;align-items:center;gap:10px;
}
.brand-mark{width:22px;height:22px;border-radius:50%;background:var(--green)}
.brand-name{font-size:50px;font-weight:700;color:var(--ink);letter-spacing:-1px;line-height:1}
.main-nav{
  position:absolute;right:92px;top:72px;
  display:flex;gap:11px;list-style:none;
}
.main-nav a{
  display:block;height:26px;padding:0 11px;
  background:var(--nav-bg);
  font-size:16px;line-height:26px;color:var(--ink);text-decoration:none;
}
.main-nav .is-active a{border-bottom:1px solid #9a9a9a}
/* Stage */
.stage{
  position:absolute;left:0;top:160px;width:1200px;height:760px;
  background:
    radial-gradient(ellipse 500px 160px at 820px 40px,rgba(225,205,195,.55),transparent 70%),
    linear-gradient(to bottom,var(--stage-top) 0%,#aab4bb 12%,var(--stage-mid) 70%,var(--stage-bottom) 100%);
}
/* Slider */
.slide-peek{position:absolute;top:290px;height:271px}
.slide-peek--prev{
  left:0;width:107px;
  background:linear-gradient(135deg,#dfe6ee 0%,#9fb6d0 55%,#e4c5b3 100%);
  opacity:.8;
}
.slide-peek--next{
  left:1108px;width:92px;
  background:linear-gradient(90deg,#f0efed 0%,#f0efed 20%,var(--tan) 22%,#a89268 100%);
  border-radius:60px 0 0 60px / 140px 0 0 140px;
}
.peek-dots{position:absolute;left:1115px;top:497px;display:flex;flex-direction:column;gap:6px}
.peek-dots span{width:10px;height:10px;border-radius:50%;background:var(--dot)}
.peek-dots span:first-child{background:#aab0b4}
.hero-slide{
  position:absolute;left:106px;top:250px;width:1002px;height:343px;
  background:var(--white);border-radius:4px;overflow:hidden;
}
.hero-photo{
  position:absolute;left:580px;top:0;width:422px;height:343px;
  background:linear-gradient(120deg,#e6ecf1 0%,#cfd8e2 35%,#e2b9a2 60%,#2b2f35 78%,#e8c2ab 100%);
}
.hero-shape{position:absolute;left:0;top:0}
.hero-copy{position:absolute;left:116px;top:42px;width:480px;color:var(--white)}
.hero-title{font-size:36px;font-weight:700;line-height:1.2}
.hero-text{margin-top:26px;font-size:20px;line-height:31px;white-space:nowrap}
.hero-link{margin-top:38px;display:flex;align-items:center;gap:18px;font-size:21px;color:var(--white);text-decoration:none}
.slider-dots{position:absolute;left:12px;top:258px;display:flex;flex-direction:column;gap:8px}
.slider-dots span{width:13px;height:13px;border-radius:50%;background:var(--dot)}
.slider-dots .is-current{background:var(--dot-active)}
/* Intro */
.intro{
  position:absolute;left:108px;top:666px;
  font-size:18px;line-height:31px;color:var(--ink-soft);white-space:nowrap;
}
.get-in-touch{
  position:absolute;left:864px;top:650px;width:246px;height:124px;text-decoration:none;
}
.get-in-touch-box{
  position:absolute;left:0;top:10px;width:244px;height:108px;
  background:linear-gradient(to bottom,#ffffff,#d9d9d9);
  box-shadow:0 1px 3px rgba(0,0,0,.25);
}
.get-in-touch-art{
  position:absolute;left:0;top:10px;width:90px;height:108px;
  background:linear-gradient(135deg,#f4f4f4,#c4c4c4);
}
.get-in-touch-label{
  position:absolute;right:26px;top:22px;text-align:right;
  font-size:48px;font-weight:700;letter-spacing:-4px;line-height:40px;
}
.get-in-touch-label .line-one{display:block;color:var(--ink)}
.get-in-touch-label .line-two{display:block;color:var(--green)}
/* Feature cards */
.features{position:absolute;left:106px;top:852px;display:flex;gap:24px}
.feature-card{
  width:318px;height:80px;background:var(--white);
  border-top:2px solid var(--green);padding:16px 14px 0;
}
.feature-title{font-size:19px;font-weight:700;color:var(--ink)}
.feature-image{margin-top:14px;height:40px;width:288px}
.feature-image--people{background:linear-gradient(90deg,#c9c2bb,#e9e4df)}
.feature-image--sms{background:linear-gradient(90deg,#b48fe0,#5fd3f0 70%,#3aa4d8)}
.feature-image--analytics{background:linear-gradient(90deg,#4c5d74,#8aa0b8)}
</style>
</head>
<body>
<header class="site-header">
  <div class="brand">
    <span class="brand-mark"></span>
    <span class="brand-name">Tornacell</span>
  </div>
  <ul class="main-nav">
    <li class="is-active"><a href="#">Home</a></li>
    <li><a href="#">Why Mobile</a></li>
    <li><a href="#">What We Do</a></li>
    <li><a href="#">News</a></li>
    <li><a href="#">Contact</a></li>
  </ul>
</header>

<main class="stage" role="img" aria-label="Soft blurred photo of a hand reaching toward a screen in pale grey-blue tones"></main>

<div class="slide-peek slide-peek--prev" role="img" aria-label="Previous slide: hand holding a smartphone showing a social feed"></div>
<div class="slide-peek slide-peek--next" role="img" aria-label="Next slide in warm tan tones"></div>
<div class="peek-dots"><span></span><span></span><span></span><span></span></div>

<section class="hero-slide">
  <div class="hero-photo" role="img" aria-label="Hand holding a smartphone displaying a social network page"></div>
  <svg class="hero-shape" width="1002" height="343" viewBox="0 0 1002 343" aria-hidden="true">
    <ellipse cx="344" cy="172" rx="322" ry="350" fill="var(--green)"/>
  </svg>
  <div class="hero-copy">
    <h1 class="hero-title">Torna Studio Model</h1>
    <p class="hero-text">Lorem ipsum dolor sit amet, consectetur adipisi-<br>cing elit, sed do eiusmod tempor incididunt ut<br>labore et dolore magna aliqua.</p>
    <a class="hero-link" href="#">
      <svg width="30" height="30" viewBox="0 0 30 30" aria-hidden="true">
        <circle cx="15" cy="15" r="13.5" fill="none" stroke="#fff" stroke-width="2.5"/>
        <path d="M8 15 H21 M16 10 L21 15 L16 20" fill="none" stroke="#fff" stroke-width="2.5" stroke-linecap="round" stroke-linejoin="round"/>
      </svg>
      Find out details
    </a>
  </div>
  <div class="slider-dots"><span class="is-current"></span><span></span><span></span><span></span></div>
</section>

<p class="intro">TornaCell is a mobile marketing company offering mobile optimized websites,<br>sms marketing, strategic and analytic consultation services. We are a b2b model<br>targeting a wide range of industries and business sizes.</p>

<a class="get-in-touch" href="#">
  <div class="get-in-touch-box"></div>
  <div class="get-in-touch-art" role="img" aria-label="Silver upward arrow illustration"></div>
  <span class="get-in-touch-label"><span class="line-one">get in</span><span class="line-two">touch</span></span>
</a>

<section class="features">
  <article class="feature-card">
    <h2 class="feature-title">Personal Experience</h2>
    <div class="feature-image feature-image--people" role="img" aria-label="Photo of a consultant at work"></div>
  </article>
  <article class="feature-card">
    <h2 class="feature-title">SMS Marketing Services</h2>
    <div class="feature-image feature-image--sms" role="img" aria-label="Colourful abstract light image for text messaging"></div>
  </article>
  <article class="feature-card">
    <h2 class="feature-title">Analytics &amp; Mapping</h2>
    <div class="feature-image feature-image--analytics" role="img" aria-label="Dark blue image of data analytics"></div>
  </article>
</section>
</body>
</html>
```